Podcast Cover Art for Inspiring Fun Show

Title: The Dave R Hour

I am looking for a simple design that includes the following:

1. Picture of me (the one I attached with the background removed) on a simple background (please refer to attachments for ideas).
2. The title done in professional lettering that is easy to read and stands out on the background

Please see attached pictures for:

1) Other podcast art I like
2) Backgrounds that I like
3) A picture of me (please edit out the background)

Target Market(s)

Anyone into personal-development, inspiring content and motivational stories.

Font styles to use
Sans Serif

Colors

Designer to choose colors to be used in the design.

Requirements
Must have
• - Title "The Dave R Hour" in professional lettering that is large and very easy to read
• - Picture of me on the background

```html
<!DOCTYPE html>
<html lang="en">
<head>
<meta charset="utf-8">
<title>The Dave R Hour – Podcast Cover</title>
<link rel="stylesheet" href="https://fonts.googleapis.com/css2?family=Josefin+Sans:wght@100&family=Montserrat:wght@800&display=swap">
<style>
  :root {
    --title-yellow: #f6d90f;
    --bg-white: #ffffff;
    --wood-light: #e4e4e4;
    --wood-mid: #cfcfcf;
    --photo-dark: #3d3f44;
    --photo-mid: #8a7f78;
  }
  html, body {
    margin: 0;
    padding: 0;
    overflow: hidden;
    background: var(--bg-white);
  }
  .cover {
    position: relative;
    width: 1200px;
    height: 1200px;
    overflow: hidden;
    background: linear-gradient(180deg,
      var(--bg-white) 0%,
      var(--bg-white) 18%,
      var(--wood-light) 45%,
      var(--wood-mid) 100%);
  }
  .wood-backdrop {
    position: absolute;
    inset: 0;
  }
  .host-photo {
    position: absolute;
    right: 0;
    bottom: 0;
    width: 640px;
    height: 1010px;
  }
  .show-title {
    position: absolute;
    left: 72px;
    top: 78px;
    margin: 0;
    color: var(--title-yellow);
    z-index: 2;
    font-weight: normal;
  }
  .show-title span { display: block; }
  .title-article {
    font-family: "Josefin Sans", sans-serif;
    font-weight: 100;
    font-size: 124px;
    line-height: 1;
    letter-spacing: 2px;
  }
  .title-name {
    font-family: "Montserrat", sans-serif;
    font-weight: 800;
    font-size: 182px;
    line-height: 0.95;
    letter-spacing: 2px;
    margin-top: 6px;
  }
  .title-format {
    font-family: "Montserrat", sans-serif;
    font-weight: 800;
    font-size: 164px;
    line-height: 1;
    letter-spacing: 1px;
    margin-top: 14px;
  }
</style>
</head>
<body>
  <main class="cover">
    <svg class="wood-backdrop" viewBox="0 0 1200 1200" aria-hidden="true">
      <g stroke="#c2c2c2" stroke-width="2" opacity="0.35">
        <line x1="100" y1="300" x2="100" y2="1200"/>
        <line x1="240" y1="300" x2="240" y2="1200"/>
        <line x1="390" y1="300" x2="390" y2="1200"/>
        <line x1="540" y1="300" x2="540" y2="1200"/>
        <line x1="1030" y1="300" x2="1030" y2="1200"/>
      </g>
    </svg>

    <svg class="host-photo" viewBox="0 0 640 1010" role="img" aria-label="Cut-out portrait photo of Dave R smiling, wearing a grey hoodie over a checked shirt">
      <defs>
        <linearGradient id="hostTone" x1="0" y1="0" x2="0" y2="1">
          <stop offset="0" stop-color="var(--photo-dark)"/>
          <stop offset="0.18" stop-color="var(--photo-mid)"/>
          <stop offset="0.65" stop-color="var(--photo-mid)"/>
          <stop offset="0.72" stop-color="var(--photo-dark)"/>
          <stop offset="1" stop-color="var(--photo-dark)"/>
        </linearGradient>
      </defs>
      <path fill="url(#hostTone)" d="M70 240 C70 90 190 20 320 20 C450 20 560 90 560 250 L560 470 C560 600 500 680 430 700 L640 820 L640 1010 L0 1010 L0 860 C60 800 160 760 220 720 C150 680 90 600 80 470 Z"/>
    </svg>

    <h1 class="show-title">
      <span class="title-article">THE</span>
      <span class="title-name">DAVE R</span>
      <span class="title-format">HOUR</span>
    </h1>
  </main>
</body>
</html>
```